PPT Template for an investment fund to use in their pitchbooks

Our firm is an international investment fund and are seeking a PPT template to use in our pitch book (and subsequent PPTs). We would need a template for a title slide and then subsequent text/info slides. A clean & uncluttered feel is preferred as well as no watermark on slides. Please see our logo attached. The logo color code is #19478d. Font is Gotham-Medium.

Target Market(s)

Sophisticated investors

Industry/Entity Type

Finance

Colors
ffffff
0356a4

```html
<!DOCTYPE html>
<html lang="en">
<head>
<meta charset="utf-8">
<title>Investment Pitch — Title Slide</title>
<link href="https://fonts.googleapis.com/css2?family=Montserrat:wght@500;600&display=swap" rel="stylesheet">
<style>
  :root {
    --brand-blue: #1b478d;
    --text-light: #ffffff;
    --bg-center: #f4f4f4;
    --bg-edge: #c9c9c9;
  }
  html, body {
    margin: 0;
    padding: 0;
    overflow: hidden;
  }
  .slide {
    position: relative;
    width: 1200px;
    height: 675px;
    overflow: hidden;
    background: radial-gradient(ellipse 70% 60% at 50% 85%, var(--bg-center) 0%, var(--bg-edge) 100%);
    font-family: "Montserrat", sans-serif;
  }
  .hero-shape {
    position: absolute;
    inset: 0;
    width: 1200px;
    height: 675px;
  }
  .hero-shape path {
    fill: var(--brand-blue);
  }
  .slide-title {
    position: absolute;
    left: 0;
    right: 0;
    top: 235px;
    margin: 0;
    text-align: center;
    color: var(--text-light);
    font-weight: 500;
    font-size: 88px;
    letter-spacing: 1px;
    line-height: 1;
  }
  .slide-subtitle {
    position: absolute;
    left: 0;
    right: 0;
    top: 365px;
    margin: 0;
    text-align: center;
    color: var(--text-light);
    font-weight: 500;
    font-size: 33px;
    line-height: 1;
  }
  .brand {
    position: absolute;
    right: 28px;
    bottom: 34px;
    display: flex;
    align-items: center;
    gap: 8px;
    color: var(--brand-blue);
    font-weight: 600;
    font-size: 15px;
    letter-spacing: 0.5px;
  }
  .brand-mark {
    width: 12px;
    height: 12px;
    background: var(--brand-blue);
  }
</style>
</head>
<body>
  <section class="slide">
    <svg class="hero-shape" viewBox="0 0 1200 675" aria-hidden="true">
      <path d="M0 0 H1200 V300 C1170 440 900 550 600 553 C300 550 30 440 0 300 Z"/>
    </svg>
    <h1 class="slide-title">Investment Pitch</h1>
    <p class="slide-subtitle">Sample Subtitle</p>
    <div class="brand">
      <span class="brand-mark"></span>
      <span class="brand-name">BASTION CLAIMS CAPITAL</span>
    </div>
  </section>
</body>
</html>
```